Electronic Letterhead for The Harbinger Partners, LLC

I would like to have an electronic letterhead layout using Word for first and second page letterhead using my previously designed logo. The logo was successfully designed by a designer for the Pixel Bazaar. I would like to only use the "C" portion of the logo on the second page. I would like the designer that designed my logo to be included in the designers that participate in this competition.

Target Market(s)

My clients are typically governmental entities or financial entities

Industry/Entity Type

Electronic

Font styles to use
Sans Serif

Requirements
Must have
• Utilize existing logo
Nice to have
• Fist and second page letterhead design in electronic format (Word)

```html
<!DOCTYPE html>
<html lang="en">
<head>
<meta charset="utf-8">
<title>The Harbinger Partners, LLC – Letterhead</title>
<link href="https://fonts.googleapis.com/css2?family=Questrial&display=swap" rel="stylesheet">
<style>
  :root {
    --backdrop: #ebebeb;
    --paper: #f8f8f8;
    --brand-blue: #2e4e8f;
    --brand-grey: #7b7b7b;
    --ink: #4a4a4a;
  }
  html, body {
    margin: 0;
    padding: 0;
    width: 1200px;
    height: 815px;
    overflow: hidden;
    background: var(--backdrop);
    font-family: "Questrial", "Century Gothic", sans-serif;
  }
  p, address { margin: 0; font-style: normal; }
  .canvas {
    position: relative;
    width: 1200px;
    height: 815px;
  }
  .sheet {
    position: absolute;
    top: 70px;
    width: 484px;
    height: 684px;
    background: var(--paper);
  }
  .sheet--first { left: 80px; }
  .sheet--second { left: 638px; }

  .accent-bar {
    position: absolute;
    background: var(--brand-blue);
    width: 8px;
  }
  .sheet--first .accent-bar { left: 0; top: 44px; height: 57px; }
  .sheet--second .accent-bar { right: 1px; top: 42px; height: 34px; }

  .brand {
    position: absolute;
    display: flex;
    align-items: center;
    gap: 9px;
    color: var(--brand-blue);
  }
  .sheet--first .brand { left: 260px; top: 52px; }
  .brand__dot {
    width: 40px;
    height: 40px;
    border-radius: 50%;
    background: var(--brand-blue);
    flex: none;
  }
  .brand__name {
    font-size: 15px;
    line-height: 17px;
    letter-spacing: 0.3px;
    text-transform: uppercase;
  }
  .sheet--second .brand { right: 20px; top: 50px; }
  .sheet--second .brand__name {
    font-size: 10px;
    line-height: 12px;
    text-align: right;
  }

  .web-address {
    position: absolute;
    font-size: 7.5px;
    line-height: 9px;
    letter-spacing: 1.6px;
    color: var(--brand-blue);
    white-space: nowrap;
  }
  .sheet--first .web-address { left: 56px; top: 658px; }
  .sheet--second .web-address { left: 92px; top: 657px; }

  .contact {
    position: absolute;
    left: 259px;
    top: 648px;
    font-size: 6.5px;
    line-height: 11px;
    color: var(--ink);
    white-space: nowrap;
  }
  .contact__row { display: flex; align-items: center; gap: 3px; }
  .contact__item { display: inline-flex; align-items: center; gap: 3px; margin-right: 5px; }
  .contact svg { width: 7px; height: 7px; }

  .base-bar {
    position: absolute;
    bottom: 0;
    height: 7px;
    background: var(--brand-grey);
  }
  .sheet--first .base-bar { left: 259px; right: 0; }
  .sheet--second .base-bar { left: 0; width: 223px; height: 8px; }
</style>
</head>
<body>
<main class="canvas">

  <section class="sheet sheet--first" aria-label="First page letterhead">
    <div class="accent-bar"></div>
    <div class="brand">
      <span class="brand__dot"></span>
      <span class="brand__name">The Harbinger<br>Partners, LLC</span>
    </div>
    <p class="web-address">www.harbinger-llc.example</p>
    <address class="contact">
      <div class="contact__row">1875 Alder Row #6 Dallas, TX 75210</div>
      <div class="contact__row">
        <span class="contact__item">
          <svg viewBox="0 0 10 10" aria-hidden="true"><circle cx="5" cy="5" r="4.4" fill="none" stroke="var(--brand-blue)" stroke-width="0.9"/><path d="M3.4 2.8 L4.3 2.6 L4.7 3.9 L4.1 4.3 Q4.6 5.5 5.7 5.9 L6.1 5.3 L7.4 5.7 L7.2 6.6 Q5.6 7.4 4 5.9 Q2.6 4.4 3.4 2.8Z" fill="var(--brand-blue)"/></svg>
          +971 4 555 0142
        </span>
        <span class="contact__item">
          <svg viewBox="0 0 10 10" aria-hidden="true"><circle cx="5" cy="5" r="5" fill="var(--brand-blue)"/><rect x="2.4" y="3.2" width="5.2" height="3.6" fill="none" stroke="#fff" stroke-width="0.7"/><path d="M2.4 3.2 L5 5.2 L7.6 3.2" fill="none" stroke="#fff" stroke-width="0.7"/></svg>
          info@harbinger-llc.example
        </span>
      </div>
    </address>
    <div class="base-bar"></div>
  </section>

  <section class="sheet sheet--second" aria-label="Second page letterhead">
    <div class="brand">
      <span class="brand__name">The Harbinger<br>Partners, LLC</span>
    </div>
    <div class="accent-bar"></div>
    <p class="web-address">www.harbinger-llc.example</p>
    <div class="base-bar"></div>
  </section>

</main>
</body>
</html>
```